Brio 41 specialty coffee shop business card

Please use Design #5812047 from previous project (logo design). Brio 41 is a new coffee shop that will serve specialty coffee and will focus on high quality products. I would like to use orange and brown colors. I like designs that are simple but elegant and that deliver a message that is easy to recognize. I will upload a file of the logo design.

Industry/Entity Type

Coffee Shop

Contact Information for Business Card

Leon Cordravik
(555) 203-7719

Font styles to use
Serif
Sans Serif
Script

Requirements
Must have
• simple and elegant, colors match nicely, I like to use orange and brown. Background creme color.
Should not have
• complex designs that are hard to understand.

```html
<!DOCTYPE html>
<html lang="en">
<head>
<meta charset="utf-8">
<title>Brio 41 – Business Card</title>
<link rel="stylesheet" href="https://fonts.googleapis.com/css2?family=Allura&family=Lato:wght@400&display=swap">
<style>
  :root {
    --backdrop: #d6d6d6;
    --card-cream: #fbf6d3;
    --card-cream-light: #fffbe6;
    --espresso: #4a3426;
    --latte: #b3946f;
    --card-shadow: rgba(0, 0, 0, 0.28);
  }
  * { box-sizing: border-box; margin: 0; padding: 0; }
  html, body {
    width: 1200px;
    height: 852px;
    overflow: hidden;
  }
  body {
    background: var(--backdrop);
    display: flex;
    flex-direction: column;
    align-items: center;
    justify-content: center;
    gap: 44px;
  }
  .business-card {
    position: relative;
    width: 630px;
    height: 360px;
    border-radius: 22px;
    background: linear-gradient(135deg, var(--card-cream-light) 0%, var(--card-cream) 60%);
    box-shadow: 0 4px 10px var(--card-shadow);
    overflow: hidden;
  }
  .brand-mark {
    display: flex;
    align-items: center;
    gap: 14px;
    color: var(--espresso);
    font-family: "Allura", cursive;
    font-weight: 400;
    line-height: 1;
  }
  .brand-mark .brand-dot {
    width: 22px;
    height: 22px;
    border-radius: 50%;
    background: var(--latte);
    flex: none;
  }
  .card-front .brand-mark {
    position: absolute;
    left: 50%;
    top: 50%;
    transform: translate(-50%, -50%);
    font-size: 96px;
  }
  .card-back .brand-mark {
    position: absolute;
    left: 50px;
    top: 50%;
    transform: translateY(-50%);
    font-size: 84px;
  }
  .contact-block {
    position: absolute;
    left: 380px;
    top: 150px;
    color: var(--espresso);
  }
  .contact-name {
    font-family: "Allura", cursive;
    font-size: 40px;
    line-height: 1.1;
  }
  .contact-phone {
    font-family: "Lato", sans-serif;
    font-size: 17px;
    letter-spacing: 1px;
    margin-top: 6px;
  }
</style>
</head>
<body>
  <section class="business-card card-front" aria-label="Card front">
    <div class="brand-mark"><span class="brand-dot"></span>Brio 41</div>
  </section>

  <section class="business-card card-back" aria-label="Card back">
    <div class="brand-mark"><span class="brand-dot"></span>Brio 41</div>
    <div class="contact-block">
      <p class="contact-name">Leon Cordravik</p>
      <p class="contact-phone">(555) 203-7719</p>
    </div>
  </section>
</body>
</html>
```